Need Website Design for Non-Profit Veteran Site

I am looking for a very talented creative website designer for a modern feel. I'll give a little bit of guidance around what I am looking for and then your creative juices should kick in and design away. I have already purchased the domain but will need hosting (at least temporarily) and the creative design work done.The website domain is militarydocs.orgI am looking to attract current and veteran military providers (doctors, nurse practitioners, physician assistants, etc) to join and signup for membership. They would pay a yearly fee to join. Would need membership categories $135 for Provider, $55 Student, $100 for Retired, and Organization (Organization would be broken down into Less than 100 ($200), 100-249 ($250), 250-499 ($300), 500-999 ($400), 1,000-2,999 ($500), and 3,000 ($700). Would need Benefit built out and would need to accept money through CoinLoft and other means. Since it's a new organization just starting, would also need a Donate button to get people to donate if they want any amount they would like. The second part of the website is that once they join, they will have acess to a list of all other providers who have registered within the website (not exportable) so they can connect with one another. If they want to see contact information this will be included in their fee as a benefit to socialize with one another. As part of the website, there will be another Veteran's portal so veterans who would like to connect with a provider around a particular speciality can reach out and request help from the doctor writing a nexus letter or letter to support the veteran who is filing a claim with the BR. Veterans would pay a yearly sign-up fee of $30.00 and would need their membership benefits displayed. They would have access to a list of veterans in their region by state and distance, and can reach out to doctors to get their help. If a doctor and veteran agree, sharable inforamtion of medical hipaa documents can be exchanged via the website. The physician and veteran can negotiate a fee through the website only and share their details. This is a separate fee for this type of process between the provider and veteran. We will collect a $250 fee for admin on each of these and each project the veteran does with the provider will cost $450 (so essentially the doctor gets paid $450 and i get $250.00. This model could be changed over time as we start to test this out). A good example of 50% of what I'm looking for is something like the following website: https://www.qelt.org/ It has some of the features but not all and my site should be more modernized to attract the veteran and military providers.

Target Market(s)

Current and retired military providers and veterans

Industry/Entity Type

Non Profit

Number of Pages Required

1 page

Requirements
Must have
• Military Design
• Modern Feel (Example templates for feel -https://brindlewax.com/free-layout-kit-template/)
• Donation box
• Stuff mentioned in the description)
Nice to have
• Open to feedback
Should not have
• Open to feedback

```html
<!DOCTYPE html>
<html lang="en">
<head>
<meta charset="utf-8">
<title>Harbor Vault</title>
<link rel="stylesheet" href="https://fonts.googleapis.com/css2?family=Roboto:wght@400;500&family=Roboto+Condensed:wght@400;700&family=Open+Sans:wght@400;600&display=swap">
<style>
:root{
  --brand-blue:#0c4a8c;
  --nav-top:#2a74bc;
  --nav-bottom:#14538f;
  --accent-red:#c3173a;
  --page-bg:#f2f2f2;
  --card-bg:#ffffff;
  --text-dark:#222222;
  --text-body:#444444;
  --line:#dcdcdc;
  --footer-bg:#0f0f0f;
  --footer-text:#e8e8e8;
  --camo-a:#5f6b3c;
  --camo-b:#2f3a22;
}
*{box-sizing:border-box;margin:0;padding:0}
html,body{width:840px;height:1200px;overflow:hidden}
body{position:relative;font-family:"Open Sans",sans-serif;color:var(--text-body);background:var(--footer-bg)}
.backdrop{position:absolute;left:0;top:0;width:840px;height:977px;background:linear-gradient(135deg,#7a8550 0%,var(--camo-a) 35%,var(--camo-b) 65%,#8a8e5a 100%)}
.page{position:absolute;left:59px;top:0;width:720px;height:977px;background:var(--page-bg)}
.header{position:absolute;left:0;top:0;width:720px;height:80px}
.logo{position:absolute;left:29px;top:24px;font-family:"Roboto Condensed",sans-serif;font-weight:700;font-size:28px;color:var(--brand-blue);letter-spacing:.5px}
.phone{position:absolute;left:426px;top:32px;font-family:"Roboto",sans-serif;font-size:14px;color:var(--text-dark);display:flex;align-items:center;gap:7px}
.btn{position:absolute;top:24px;height:31px;color:#fff;font-family:"Open Sans",sans-serif;font-size:13px;display:flex;align-items:center;justify-content:center;border-radius:2px}
.btn-join{left:554px;width:66px;background:var(--accent-red)}
.btn-signup{left:626px;width:78px;background:var(--brand-blue)}
.nav{position:absolute;left:0;top:80px;width:720px;height:42px;background:linear-gradient(var(--nav-top),var(--nav-bottom));display:flex;align-items:center;padding-left:45px;gap:0}
.nav a{color:#fff;text-decoration:none;font-family:"Roboto",sans-serif;font-size:12.5px}
.hero{position:absolute;left:0;top:122px;width:720px;height:376px;background:linear-gradient(90deg,#a9aca3 0%,#8e8d84 45%,#4d4a3c 75%,#3b3a2e 100%)}
.hero-title{position:absolute;left:37px;top:228px;font-family:"Roboto Condensed",sans-serif;font-weight:700;font-size:32px;color:#fff}
.hero-sub{position:absolute;left:37px;top:266px;font-family:"Roboto Condensed",sans-serif;font-size:21px;color:#fff}
.hero-arrows{position:absolute;left:642px;top:296px;display:flex;gap:3px}
.hero-arrows span{width:14px;height:14px;border-radius:50%;background:rgba(255,255,255,.35);color:#fff;font-size:10px;display:flex;align-items:center;justify-content:center}
.welcome{position:absolute;left:17px;top:450px;width:678px;height:211px;background:var(--card-bg);box-shadow:0 2px 6px rgba(0,0,0,.18)}
.welcome-photo{position:absolute;left:0;top:0;width:222px;height:211px;background:linear-gradient(135deg,#dfe6ec,#b9c4cc 60%,#e9ecef)}
.welcome-body{position:absolute;left:251px;top:22px;width:391px}
.welcome h1{font-family:"Roboto",sans-serif;font-weight:400;font-size:23px;color:var(--text-dark);margin-bottom:11px}
.welcome p{font-size:9.8px;line-height:15.8px;text-align:justify;color:var(--text-body)}
.btn-veterans{display:inline-block;margin-top:12px;padding:6px 8px;background:var(--brand-blue);color:#fff;font-size:11px;border-radius:2px}
.panel{position:absolute;top:706px;height:230px;background:var(--card-bg);border:1px solid var(--line)}
.donate{left:19px;width:211px;padding:3px;box-shadow:0 1px 3px rgba(0,0,0,.15)}
.donate-inner{position:relative;width:100%;height:100%;background:linear-gradient(160deg,#d03a62,#b8163e);color:#fff;text-align:center}
.donate h2{position:absolute;top:52px;width:100%;font-family:"Roboto",sans-serif;font-weight:500;font-size:25px}
.donate p{position:absolute;top:90px;left:18px;right:18px;font-family:"Roboto",sans-serif;font-size:10.8px;line-height:17px}
.donate-btn{position:absolute;left:69px;top:148px;width:68px;height:25px;border:1px solid #fff;border-radius:2px;display:flex;align-items:center;justify-content:center;font-family:"Roboto",sans-serif;font-size:12px}
.benefits{left:250px;width:211px}
.news{left:482px;width:211px}
.panel h3{height:35px;background:linear-gradient(#ffffff,#ececec);border-bottom:1px solid var(--line);font-family:"Roboto",sans-serif;font-weight:400;font-size:14.5px;color:var(--text-dark);padding:10px 16px}
.benefit-list{list-style:none;padding:14px 0 0 20px}
.benefit-list li{font-family:"Roboto",sans-serif;font-size:10px;color:var(--text-body);height:24px;display:flex;gap:6px}
.benefit-list li::before{content:"»";color:var(--accent-red)}
.news-list{list-style:none;padding:16px 14px 0 16px}
.news-list li{display:flex;gap:9px;font-family:"Roboto",sans-serif;font-size:10px;line-height:13.5px;color:var(--text-body);margin-bottom:13px}
.news-list svg{flex:none;margin-top:2px}
.footer{position:absolute;left:0;top:977px;width:840px;height:223px;background:var(--footer-bg);color:var(--footer-text);font-family:"Open Sans",sans-serif}
.footer-logo{position:absolute;left:78px;top:90px;font-family:"Roboto Condensed",sans-serif;font-weight:700;font-size:21px;color:#fff}
.footer h4{position:absolute;top:55px;font-weight:400;font-size:10px;letter-spacing:.2px}
.contact-list{position:absolute;left:261px;top:83px;list-style:none;font-size:8.5px;line-height:13.5px}
.contact-list li{display:flex;gap:9px;margin-bottom:4px}
.contact-list svg{flex:none;margin-top:2px}
.mail-note{position:absolute;left:438px;top:82px;width:160px;font-size:8.5px;line-height:11.5px}
.mail-form{position:absolute;left:438px;top:105px;display:flex}
.mail-input{width:111px;height:22px;background:#fff;color:#999;font-size:8px;padding:6px 6px}
.mail-submit{width:44px;height:22px;background:var(--brand-blue);color:#fff;font-size:8.5px;display:flex;align-items:center;justify-content:center}
.social{position:absolute;left:648px;top:92px;display:flex;gap:10px}
.social span{width:17px;height:17px;border-radius:3px;background:#fff}
.footer-rule{position:absolute;left:67px;top:169px;width:716px;height:1px;background:#2b2b2b}
.copyright{position:absolute;left:0;top:195px;width:840px;text-align:center;font-size:8.5px}
</style>
</head>
<body>
<div class="backdrop" role="img" aria-label="Olive green geometric camouflage background"></div>
<main class="page">
  <header class="header">
    <div class="logo">HARBOR VAULT</div>
    <div class="phone">
      <svg width="10" height="10" viewBox="0 0 24 24"><path fill="#c3173a" d="M6.6 10.8a15 15 0 0 0 6.6 6.6l2.2-2.2c.3-.3.7-.4 1-.2 1.1.4 2.3.6 3.6.6.6 0 1 .4 1 1V20c0 .6-.4 1-1 1A17 17 0 0 1 3 4c0-.6.4-1 1-1h3.5c.6 0 1 .4 1 1 0 1.3.2 2.5.6 3.6.1.3 0 .7-.2 1z"/></svg>
      (555) 318-2704
    </div>
    <div class="btn btn-join">JOIN</div>
    <div class="btn btn-signup">SIGNUP</div>
  </header>
  <nav class="nav">
    <a style="width:88px">HOME</a><a style="width:111px">ABOUT US</a><a style="width:109px">SERVICES</a><a style="width:77px">FAQ</a><a style="width:85px">BLOG</a><a style="width:107px">SUPPORT</a><a>CONTACT</a>
  </nav>
  <section class="hero" role="img" aria-label="Photo of a young soldier in camouflage with a doctor in a white coat behind him">
    <div class="hero-title">HARBOR VAULT</div>
    <div class="hero-sub">Dolorem ipsum quia dolor sit amet</div>
    <div class="hero-arrows"><span>‹</span><span>›</span></div>
  </section>
  <section class="welcome">
    <div class="welcome-photo" role="img" aria-label="Photo of a smiling senior doctor leaning on a desk in a clinic"></div>
    <div class="welcome-body">
      <h1>Welcome to Harbor Vault</h1>
      <p>It is a long established fact that a reader will be distracted by the readable content of a page when looking at its layout. The point of using Lorem Ipsum is that it has a more-or-less normal distribution of letters, as opposed to using 'Content here, content here', making it look like readable English. Many desktop publishing packages and web page editors now use Lorem Ipsum as their default model text, and a search for 'lorem ipsum' will uncover many web sites still in their infancy.</p>
      <span class="btn-veterans">Veterans Sign-up</span>
    </div>
  </section>
  <section class="panel donate">
    <div class="donate-inner" role="img" aria-label="Red tinted photo of hands holding a heart">
      <h2>Donate</h2>
      <p>Neque porro quisquam est qui dolorem ipsum quia dolor sit amet, consectetur, adipisci velit</p>
      <div class="donate-btn">Donate</div>
    </div>
  </section>
  <section class="panel benefits">
    <h3>Benefits</h3>
    <ul class="benefit-list">
      <li>Lorem ipsum dolor sit amet,</li>
      <li>Phasellus suscipit massa quis</li>
      <li>Curabitur varius mi eu nisl facilisis</li>
      <li>Ut quis tellus sed ligula efficitur</li>
      <li>Sed aliquam nulla in laoreet</li>
      <li>Etiam a ipsum a leo efficitur laoreet.</li>
      <li>Curabitur cursus elit risus tempus</li>
    </ul>
  </section>
  <section class="panel news">
    <h3>Latest News</h3>
    <ul class="news-list">
      <li><svg width="9" height="9" viewBox="0 0 10 10"><circle cx="5" cy="5" r="5" fill="#c3173a"/><path d="M4 2.8 6.2 5 4 7.2" stroke="#fff" stroke-width="1.4" fill="none"/></svg>Aenean quis odio vitae ante dictum feugiat.</li>
      <li><svg width="9" height="9" viewBox="0 0 10 10"><circle cx="5" cy="5" r="5" fill="#c3173a"/><path d="M4 2.8 6.2 5 4 7.2" stroke="#fff" stroke-width="1.4" fill="none"/></svg>Praesent non ex dapibus, interdum lorem eget, porttitor ex.</li>
      <li><svg width="9" height="9" viewBox="0 0 10 10"><circle cx="5" cy="5" r="5" fill="#c3173a"/><path d="M4 2.8 6.2 5 4 7.2" stroke="#fff" stroke-width="1.4" fill="none"/></svg>Lorem ipsum dolor sit amet, suscipit consectetur adipiscing elit</li>
      <li><svg width="9" height="9" viewBox="0 0 10 10"><circle cx="5" cy="5" r="5" fill="#c3173a"/><path d="M4 2.8 6.2 5 4 7.2" stroke="#fff" stroke-width="1.4" fill="none"/></svg>Integer faucibus ligula eget eros elementum suscipit vitae</li>
    </ul>
  </section>
</main>
<footer class="footer">
  <div class="footer-logo">HARBOR VAULT</div>
  <h4 style="left:264px">CONTACT US</h4>
  <ul class="contact-list">
    <li><svg width="7" height="9" viewBox="0 0 10 14"><path fill="#fff" d="M5 0a5 5 0 0 0-5 5c0 3.8 5 9 5 9s5-5.2 5-9a5 5 0 0 0-5-5zm0 7a2 2 0 1 1 0-4 2 2 0 0 1 0 4z"/></svg><span>1180 Alder Lane<br>Fairmont, ST 00412</span></li>
    <li><svg width="8" height="8" viewBox="0 0 24 24"><path fill="#fff" d="M6.6 10.8a15 15 0 0 0 6.6 6.6l2.2-2.2c.3-.3.7-.4 1-.2 1.1.4 2.3.6 3.6.6.6 0 1 .4 1 1V20c0 .6-.4 1-1 1A17 17 0 0 1 3 4c0-.6.4-1 1-1h3.5c.6 0 1 .4 1 1 0 1.3.2 2.5.6 3.6.1.3 0 .7-.2 1z"/></svg><span>(555) 318-2704</span></li>
    <li><svg width="8" height="7" viewBox="0 0 12 9"><rect width="12" height="9" fill="#fff"/><path d="M0 0l6 5 6-5" stroke="#0f0f0f" stroke-width="1.2" fill="none"/></svg><span>hello@harborvault.org</span></li>
  </ul>
  <h4 style="left:438px">JOIN OUR MAILING LIST</h4>
  <p class="mail-note">Your about us information would fit here nicely.</p>
  <div class="mail-form"><div class="mail-input">Email address</div><div class="mail-submit">Submit</div></div>
  <h4 style="left:648px">FOLLOW US OUT THERE</h4>
  <div class="social" aria-label="Social links"><span></span><span></span><span></span><span></span></div>
  <div class="footer-rule"></div>
  <div class="copyright">Copyright © 2018 All Rights Reserved</div>
</footer>
</body>
</html>
```